Lindavo Civic Growth Planning New web site

Design a new web site. I have a budget of $1,500.00.
Attached on PowerPoint is a complete site plan. Home page and linked pages.
10 - 12 pages. All copy and photos will be supplied. (300dpi)
I have shown them the concept which they like.
No data bases required. Home page with animations dissolving.
They former web site has been taken down. They have been in business 30 years in New Jersey
Colors teal blues and greens
There will be a new logo)being designed)
The text in home page copy will give you a detailed story what they are all about.
Updates

files have been approved for Lindavo, Inc.   Teodor is the designer

Industry/Entity Type

Community

```html
<!DOCTYPE html>
<html lang="en">
<head>
<meta charset="utf-8">
<title>Lindavo Inc. | Community Development &amp; Housing Rehabilitation</title>
<link href="https://fonts.googleapis.com/css2?family=Raleway:wght@300;400;500;600;700;800;900&display=swap" rel="stylesheet">
<style>
:root{
  --teal:#1a9396;
  --teal-dark:#147c7f;
  --ink:#1d1d1d;
  --grey:#8d8d8d;
  --grey-light:#b5b5b5;
  --footer:#353535;
  --footer-deep:#242424;
  --white:#ffffff;
}
*{margin:0;padding:0;box-sizing:border-box}
html,body{width:920px;height:1200px;overflow:hidden;background:var(--white)}
body{position:relative;font-family:'Raleway',sans-serif;color:var(--ink)}
.abs{position:absolute}

/* header */
.site-header{position:absolute;left:0;top:0;width:920px;height:67px}
.brand{left:154px;top:22px;display:flex;align-items:center;gap:7px}
.brand-mark{width:18px;height:18px;background:var(--teal)}
.brand-name{font-weight:800;font-size:22px;color:var(--teal);letter-spacing:.2px}
.phone{left:590px;top:16px;font-size:13px;color:var(--teal);font-weight:500}
.phone-sep{left:687px;top:17px;width:1px;height:11px;background:var(--ink)}
.social{left:700px;top:17px;display:flex;gap:3px}
.social span{width:14px;height:14px;border-radius:50%;background:var(--teal)}
.main-nav{left:421px;top:49px;display:flex;gap:6px;font-size:7.6px;color:#333;font-weight:500}
.main-nav .sep{color:#999}
.main-nav .active{position:relative}
.main-nav .active::after{content:"";position:absolute;left:0;right:0;top:12px;height:2px;background:var(--teal)}

/* hero */
.hero{left:0;top:67px;width:920px;height:366px;background:linear-gradient(180deg,#7fb2df 0%,#b9d6ee 38%,#e6e9e6 62%,#c9c4b9 80%,#6b8b4c 100%)}
.hero-copy{left:332px;top:113px}
.hero-lead{font-size:31px;font-weight:400;color:#111;line-height:1}
.hero-caps{font-size:28.5px;font-weight:900;color:var(--white);line-height:1;letter-spacing:-.6px;margin-top:4px}
.hero-line2{display:flex;align-items:flex-start;margin-top:-1px}
.amp{font-size:52px;font-weight:700;color:#111;line-height:.8;margin-right:1px}
.hero-sub{font-size:15px;font-weight:700;color:#111;margin-top:-2px;line-height:1}
.slider-dots{left:154px;top:398px;display:flex;gap:2px}
.slider-dots span{width:24px;height:24px;background:var(--teal);opacity:.85}

/* offer */
.offer-title{left:155px;top:478px}
.offer-what{font-size:25px;font-weight:400;color:#111;line-height:1}
.offer-big{font-size:42px;font-weight:900;color:var(--teal);line-height:.95;letter-spacing:-1px}
.offer-divider{left:305px;top:482px;height:56px;border-left:1px dotted var(--grey-light)}
.offer-list{left:318px;top:481px;list-style:none;font-size:8.6px;color:var(--grey);line-height:15.3px}
.offer-list li::before{content:"";display:inline-block;width:3px;height:3px;background:var(--grey);margin-right:5px;vertical-align:middle}

/* who we are */
.who-panel{left:0;top:580px;width:516px;height:226px;background:linear-gradient(90deg,#3a3a3a 0%,#2a2a2a 55%,#161616 100%)}
.who-copy{left:154px;top:594px;width:340px;color:var(--white)}
.who-copy h2{font-size:20px;font-weight:800;letter-spacing:.2px;padding-bottom:6px;border-bottom:1px dotted #bbb;margin-bottom:10px}
.who-copy p{font-size:8.6px;line-height:10.2px;margin-bottom:9px}
.who-copy strong{font-size:11px;font-weight:700}
.who-copy a{color:var(--teal);text-decoration:none}
.results{left:538px;top:593px;width:212px}
.results h3{font-size:14px;font-weight:500;color:var(--teal);margin-bottom:7px}
.results ul{list-style:none}
.results li{font-size:7.4px;color:var(--grey);line-height:9.4px;padding-left:10px;position:relative;margin-bottom:9.5px}
.results li::before{content:"";position:absolute;left:1px;top:2px;width:5px;height:5px;border:1px dotted var(--teal);border-radius:50%}
.teal-block{left:766px;top:580px;width:154px;height:225px;background:var(--teal)}

/* memberships */
.members-title{left:153px;top:843px;font-size:19px;font-weight:500;color:var(--teal)}
.members-rule{left:153px;top:874px;width:612px;border-top:1px dotted var(--grey-light)}
.member{top:885px;width:148px}
.member .photo{width:148px;height:93px}
.member p{font-size:8.6px;color:var(--grey);line-height:10.4px;margin-top:8px}

/* footer */
.site-footer{left:0;top:1045px;width:920px;height:118px;background:var(--footer)}
.foot-col{top:1063px;color:var(--white)}
.foot-col h4{font-size:9px;font-weight:700;margin-bottom:8px;letter-spacing:.1px}
.foot-col li{list-style:none;font-size:8.6px;line-height:15.6px;color:#e4e4e4}
.foot-sep{top:1068px;height:66px;width:1px;background:#4a4a4a}
.foot-bar{left:0;top:1163px;width:920px;height:35px;background:var(--footer-deep)}
.copyright{left:155px;top:1176px;font-size:7.6px;color:#bdbdbd}
.foot-brand{left:690px;top:1176px;font-size:12px;font-weight:800;color:#555}
</style>
</head>
<body>

<header class="site-header">
  <div class="abs brand"><span class="brand-mark"></span><span class="brand-name">Lindavo Inc.</span></div>
  <div class="abs phone">(555) 214-3380</div>
  <div class="abs phone-sep"></div>
  <div class="abs social" aria-label="Social links"><span></span><span></span><span></span><span></span></div>
  <nav class="abs main-nav">
    <span class="active">Home</span><span class="sep">//</span>
    <span>Our Company</span><span class="sep">//</span>
    <span>Housing Rehab Application</span><span class="sep">//</span>
    <span>Affordable Application</span><span class="sep">//</span>
    <span>Contact Us</span>
  </nav>
</header>

<section class="abs hero" role="img" aria-label="Row of rehabilitated single-storey homes with striped awnings and a palm tree under a blue sky"></section>
<div class="abs hero-copy">
  <div class="hero-lead">Specializes In</div>
  <div class="hero-caps">COMMUNITY DEVELOPMENT</div>
  <div class="hero-line2">
    <span class="amp">&amp;</span>
    <div>
      <div class="hero-caps" style="margin-top:0">HOUSING REHABILITATION</div>
      <div class="hero-sub">program planning, design and implementation</div>
    </div>
  </div>
</div>
<div class="abs slider-dots"><span></span><span></span></div>

<section>
  <div class="abs offer-title">
    <div class="offer-what">What We</div>
    <div class="offer-big">OFFER!</div>
  </div>
  <div class="abs offer-divider"></div>
  <ul class="abs offer-list">
    <li>Comunity Development Planing</li>
    <li>Housing Rehabilitation Administration</li>
    <li>US Department of Housing &amp; Urban Development (HUD) Program Management</li>
    <li>Implementation of Programs Under the Jurisdiction of New Jersey Council of Afforadable Housing (COAH)</li>
  </ul>
</section>

<section>
  <div class="abs who-panel" role="img" aria-label="Dimly lit office scene with a consultant meeting a client"></div>
  <div class="abs who-copy">
    <h2>WHO WE ARE!</h2>
    <p><strong>Lindavo, Inc.</strong> is a city planning firm that specializes in community development and housing rehabilitation program planning, design and implementation. We have over twenty years of experience in developing and administering income base-base housing and programs in accordance with US Department of Housing and Urban Development (HUD) and New Jersey Council on Affordable Housing (COAH) rules and regulations.</p>
    <p>In addition, our firm is capable of providing the technical and administrative assistance our clients require for implementation of their income based housing programs. M. Arlen Voss Associates is one of the most experience urban planning firms in New Jersey, with over forty years of as consulting planners.</p>
    <p>To find out more about federal housing programs that we will administer, please go to <a>www.housingdesk.info</a></p>
  </div>
  <div class="abs results">
    <h3>We Get Results!</h3>
    <ul>
      <li>Lindavo designs income based programs to be supported by federal placement lotteries state funding.</li>
      <li>We implement local programs to benefit people seeking access to affordable housing.</li>
      <li>Our experienced staff screen applicants for local affordable housing.</li>
      <li>We pre-qualify persons who have applied for housing rehabilitation.</li>
      <li>Conduct placement lotteries.</li>
      <li>Through local housing rehabilitation programs, our experience construction inspectors determine what improvements are required at eligible units based on local building codes and health and safety issues.</li>
    </ul>
  </div>
  <div class="abs teal-block"></div>
</section>

<section>
  <h2 class="abs members-title">Memberships</h2>
  <div class="abs members-rule"></div>
  <div class="abs member" style="left:153px">
    <div class="photo" role="img" aria-label="Modern brick and glass apartment building" style="background:linear-gradient(160deg,#8aa2b5,#9a6a45 55%,#5d4432)"></div>
    <p>National Civic Renewal Alliance</p>
  </div>
  <div class="abs member" style="left:308px">
    <div class="photo" role="img" aria-label="Illuminated townhouse complex at night" style="background:linear-gradient(180deg,#1b1a1e,#6d5a44 55%,#c9b79a)"></div>
    <p>Garden State Planning Guild</p>
  </div>
  <div class="abs member" style="left:464px">
    <div class="photo" role="img" aria-label="White multi-storey office buildings on a city street" style="background:linear-gradient(180deg,#cfd6dc,#e9e9e7 50%,#8c8a86)"></div>
    <p>Shoreline Planning Council</p>
  </div>
  <div class="abs member" style="left:619px">
    <div class="photo" role="img" aria-label="Aerial view of a downtown arts centre and plaza" style="background:linear-gradient(170deg,#9a9c96,#8a5d49 50%,#6f7d5d)"></div>
    <p>Coastal Community Growth League</p>
  </div>
</section>

<footer>
  <div class="abs site-footer"></div>
  <div class="abs foot-col" style="left:154px"><h4>OUR COMPANY</h4><ul><li>Bio's</li><li>Photos</li><li>Principal</li><li>Employees</li></ul></div>
  <div class="abs foot-sep" style="left:256px"></div>
  <div class="abs foot-col" style="left:294px"><h4>HOUSING REHAB APPLICATION</h4><ul><li>Lakewood</li><li>Brick</li><li>Jackson</li><li>Warren</li></ul></div>
  <div class="abs foot-sep" style="left:470px"></div>
  <div class="abs foot-col" style="left:506px"><h4>AFFORDABLE APPLICATION</h4><ul><li>Lakewood - Applicable</li><li>Brick - Applicable</li><li>Jackson - Applicable</li><li>Warren - Applicable</li></ul></div>
  <div class="abs foot-sep" style="left:667px"></div>
  <div class="abs foot-col" style="left:701px"><h4>CONTACT US</h4><ul><li>Contact Info</li><li>Directions</li><li>Sliding Map</li></ul></div>
  <div class="abs foot-bar"></div>
  <div class="abs copyright">Copy Right 2014 Lindavo, 118 Harbor Crest Avenue, Brick, New Jersey, 08700 &nbsp; TEL (555) 214-3380 Fax (555) 214-3391</div>
  <div class="abs foot-brand">Lindavo Inc.</div>
</footer>

</body>
</html>
```